" Somos uma escola de Yoga e oferecemos aulas, Cursos de Formaçao para Professores de Yoga, workshops e retiros de meditaçao pelo Brasil e em países como Costa Rica, Panamá, Bali e Tailandia. Trabalhamos com o metodo Yin e Yang.. onde yin é a energia da meditaçao, contemplaçao e observaçao e yang do movimento, rítmo, força e atividade. "

```html
<!DOCTYPE html>
<html lang="pt">
<head>
<meta charset="utf-8">
<title>Sol Lua Yoga — marcadores</title>
<link href="https://fonts.googleapis.com/css2?family=Quicksand:wght@400;600&display=swap" rel="stylesheet">
<style>
  :root {
    --canvas-bg: #eceae5;
    --leaf-green: #86b83a;
    --deep-green: #6f9e2b;
    --paper-white: #ffffff;
    --ink-dark: #3a3a3a;
    --ink-soft: #8a8a8a;
  }
  html, body {
    margin: 0;
    padding: 0;
    width: 1200px;
    height: 1200px;
    overflow: hidden;
    background: var(--canvas-bg);
    font-family: "Quicksand", sans-serif;
  }
  .bookmark-set {
    position: relative;
    width: 1200px;
    height: 1200px;
  }
  .bookmark {
    position: absolute;
    top: 120px;
    width: 300px;
    height: 960px;
  }
  .bookmark--white { left: 210px; }
  .bookmark--green { left: 690px; }
  .bookmark-shape {
    position: absolute;
    inset: 0;
    filter: drop-shadow(0 6px 14px rgba(0,0,0,0.12));
  }
  .seal-name {
    position: absolute;
    left: 0;
    width: 300px;
    top: 130px;
    text-align: center;
    font-weight: 600;
    font-size: 30px;
    line-height: 1.1;
    letter-spacing: 0.5px;
  }
  .bookmark--white .seal-name { color: var(--leaf-green); }
  .bookmark--green .seal-name { color: var(--leaf-green); }
  .brand-block {
    position: absolute;
    display: flex;
    flex-direction: column;
    align-items: center;
  }
  .bookmark--white .brand-block {
    left: 40px;
    width: 220px;
    top: 760px;
  }
  .brand-dot {
    width: 34px;
    height: 34px;
    border-radius: 50%;
    background: var(--leaf-green);
    margin-bottom: 10px;
  }
  .brand-name {
    font-size: 26px;
    font-weight: 600;
    color: var(--leaf-green);
    white-space: nowrap;
  }
  .brand-tagline {
    font-size: 13px;
    font-weight: 400;
    color: var(--ink-soft);
    letter-spacing: 2px;
    margin-top: 4px;
    white-space: nowrap;
  }
  .bookmark--green .brand-block {
    left: 150px;
    top: 780px;
    transform: translate(-50%, -50%) rotate(-90deg);
    align-items: flex-start;
    flex-direction: row;
    gap: 12px;
  }
  .bookmark--green .brand-dot { background: var(--paper-white); margin: 6px 0 0 0; width: 26px; height: 26px; }
  .bookmark--green .brand-name { color: var(--paper-white); }
  .bookmark--green .brand-tagline { color: rgba(255,255,255,0.8); }
</style>
</head>
<body>
  <main class="bookmark-set">

    <section class="bookmark bookmark--white" aria-label="Marcador branco">
      <svg class="bookmark-shape" width="300" height="960" viewBox="0 0 300 960">
        <rect x="40" y="150" width="220" height="800" fill="var(--paper-white)"/>
        <circle cx="150" cy="150" r="150" fill="var(--leaf-green)"/>
        <circle cx="150" cy="150" r="118" fill="var(--paper-white)"/>
      </svg>
      <div class="seal-name">sol lua<br>yoga</div>
      <div class="brand-block">
        <span class="brand-dot"></span>
        <span class="brand-name">sol lua yoga</span>
        <span class="brand-tagline">escola de yoga</span>
      </div>
    </section>

    <section class="bookmark bookmark--green" aria-label="Marcador verde">
      <svg class="bookmark-shape" width="300" height="960" viewBox="0 0 300 960">
        <rect x="40" y="150" width="220" height="800" fill="var(--leaf-green)"/>
        <circle cx="150" cy="150" r="150" fill="var(--leaf-green)"/>
        <circle cx="150" cy="150" r="126" fill="var(--paper-white)"/>
        <circle cx="150" cy="150" r="104" fill="none" stroke="var(--leaf-green)" stroke-width="4"/>
      </svg>
      <div class="seal-name">sol lua<br>yoga</div>
      <div class="brand-block">
        <span class="brand-dot"></span>
        <div>
          <div class="brand-name">sol lua yoga</div>
          <div class="brand-tagline">escola de yoga</div>
        </div>
      </div>
    </section>

  </main>
</body>
</html>
```